Talented Veroka Recruitment company

We require a website for job recruitment company called "Talented Veroka"
Our company is specialising in recruitment of skilled labour from Sri Lanka into Australian market.
We would like to include a job advertising plugin where jobs can be listed and applied for .
COPYWRITING MUST BE INCLUDED !

Industry/Entity Type

Recruitment

Coding

Coded - Design and coding required

Number of Pages Required

5+ page

Colors

Designer to choose colors to be used in the design.

```html
<!DOCTYPE html>
<html lang="en">
<head>
<meta charset="utf-8">
<title>Talented Veroka – Find Your Desire Job</title>
<link href="https://fonts.googleapis.com/css2?family=EB+Garamond:wght@500;600;700&family=Mulish:wght@400;500;600&display=swap" rel="stylesheet">
<style>
:root{
  --blue:#0b56a4;
  --blue-dark:#094a8e;
  --navy:#0a1a33;
  --ink:#3f4652;
  --text:#555b66;
  --muted:#8a909a;
  --line:#e3e6ea;
  --gold:#d2a70c;
  --white:#ffffff;
  --serif:'EB Garamond', Georgia, serif;
  --sans:'Mulish', Arial, sans-serif;
}
*{box-sizing:border-box;margin:0;padding:0}
html,body{width:1200px;height:3055px;overflow:hidden}
body{position:relative;background:var(--white);font-family:var(--sans);color:var(--text)}
.abs{position:absolute}
a{color:inherit;text-decoration:none}

/* header */
.site-header{position:absolute;left:0;top:0;width:1200px;height:130px;background:#fff;box-shadow:0 2px 6px rgba(0,0,0,.06);z-index:3}
.brand{position:absolute;left:134px;top:24px;font-family:var(--serif);font-weight:700;font-size:30px;color:#3d4f6b;line-height:1}
.brand small{display:block;font-size:19px;letter-spacing:4px;margin-top:2px;font-weight:700}
.contact-box{position:absolute;left:488px;top:22px;display:flex;gap:10px;align-items:center}
.contact-box .label{font-size:12px;color:var(--ink);letter-spacing:.3px}
.contact-box .phone{font-family:var(--serif);font-weight:700;font-size:23px;color:var(--blue);line-height:1}
.btn-pill{position:absolute;top:21px;height:40px;border-radius:20px;font-size:12px;letter-spacing:.6px;display:flex;align-items:center;justify-content:center;font-weight:600}
.btn-outline{left:688px;width:161px;border:1px solid #bfc4ca;color:var(--ink)}
.btn-solid{left:860px;width:204px;background:var(--blue);color:#fff}
.header-rule{position:absolute;left:134px;top:82px;width:930px;height:1px;background:var(--line)}
.main-nav{position:absolute;top:99px;font-size:13px;color:var(--ink);letter-spacing:.3px}

/* hero */
.hero{position:absolute;left:0;top:130px;width:1200px;height:633px;background:linear-gradient(180deg,#d7d8da 0%,#cfd0d2 60%,#c3c4c6 100%)}
.hero-title{position:absolute;left:0;top:52px;width:1200px;text-align:center;font-family:var(--serif);font-weight:600;font-size:66px;color:#4b4d52;letter-spacing:1px;line-height:72px}
.hero-title .tag{background:var(--blue);color:#fff;padding:0 16px;margin:0 10px;border-radius:3px}
.hero-sub{position:absolute;left:0;top:136px;width:1200px;text-align:center;font-size:19px;color:#4b4d52}
.hero-sub::before{content:"";display:inline-block;width:32px;height:1px;background:var(--blue);vertical-align:middle;margin-right:10px}
.hero-photo{position:absolute;left:20px;top:200px;width:1160px;height:433px;background:linear-gradient(90deg,#2b3e5c 0%,#7a4a45 22%,#e9ebee 48%,#6b2430 68%,#4e6048 92%);opacity:.55;border-radius:120px 120px 0 0}
.search-bar{position:absolute;left:202px;top:735px;width:794px;height:54px;background:#fff;border-radius:27px;box-shadow:0 4px 14px rgba(0,0,0,.08);z-index:2;font-size:16px;color:var(--muted)}
.search-bar .cat{position:absolute;left:24px;top:17px;display:flex;gap:8px;align-items:center}
.search-bar .sep{position:absolute;left:226px;top:14px;width:1px;height:26px;background:var(--line)}
.search-bar .kw{position:absolute;left:260px;top:17px;display:flex;gap:8px;align-items:center}
.search-bar .go{position:absolute;right:5px;top:5px;width:155px;height:44px;background:var(--blue);color:#fff;border-radius:22px;display:flex;align-items:center;justify-content:center;font-size:16px}

/* looking for */
.split-card{position:absolute;top:866px;height:278px;width:447px;background:#fff;border:1px solid var(--line);border-radius:10px;text-align:center;padding:38px 28px 0}
.split-card h2{font-family:var(--serif);font-weight:600;font-size:36px;color:#444;line-height:1}
.split-card p{margin-top:18px;font-size:15px;line-height:27.5px;color:var(--text)}
.pill-link{position:absolute;height:46px;top:1118px;background:#fff;border:1px solid #d5d9de;border-radius:23px;font-size:16px;color:var(--ink);display:flex;align-items:center;justify-content:center}
.call-line{position:absolute;left:0;top:1206px;width:1200px;text-align:center;font-size:15px;color:var(--text)}

/* featured */
.featured{position:absolute;left:0;top:1296px;width:1200px;height:659px;background:var(--blue);overflow:hidden}
.section-title{position:absolute;left:0;width:1200px;text-align:center;font-family:var(--serif);font-weight:700;font-size:45px;letter-spacing:2px;line-height:52px}
.section-title .tag{padding:0 10px;margin:0 6px;border-radius:3px}
.job-card{position:absolute;width:454px;height:197px;background:#fff;border-radius:4px}
.job-card .co{position:absolute;left:25px;top:22px;width:46px;height:46px;border-radius:50%;background:#1a83cf;color:#fff;font-size:13px;font-weight:600;display:flex;align-items:center;justify-content:center}
.job-card h3{position:absolute;left:89px;top:22px;font-family:var(--serif);font-weight:600;font-size:18px;color:var(--ink)}
.job-card .meta{position:absolute;left:89px;top:53px;font-size:14px;color:var(--text);display:flex;gap:6px;align-items:center}
.job-card .meta em{font-style:normal;color:var(--blue);margin-left:12px}
.job-card p{position:absolute;left:89px;top:82px;width:345px;font-size:14px;line-height:23px;color:var(--text)}
.job-card .apply{position:absolute;left:89px;top:146px;width:115px;height:28px;border:1px solid #7c828b;border-radius:14px;font-size:11px;letter-spacing:.5px;display:flex;align-items:center;justify-content:center;color:var(--ink)}
.job-card .badge{position:absolute;right:10px;top:10px;width:65px;height:22px;background:var(--gold);color:#fff;font-size:10px;border-radius:3px;display:flex;align-items:center;justify-content:center;font-weight:600}

/* testimonials */
.tabs{position:absolute;left:505px;top:2118px;width:190px;height:29px;border-bottom:1px solid #ccd1d7;font-size:13px;display:flex}
.tabs span{width:95px;text-align:center;color:var(--muted)}
.tabs .on{color:var(--blue);border-bottom:3px solid var(--blue)}
.quote-card{position:absolute;left:430px;top:2206px;width:533px;height:385px;background:#fff;box-shadow:0 2px 20px rgba(0,0,0,.08)}
.person-photo{position:absolute;left:312px;top:2275px;width:249px;height:246px;background:linear-gradient(180deg,#e4e5e6,#c9cacc);z-index:2}
.avatar{position:absolute;width:38px;height:38px;border-radius:50%;border:3px solid #fff;box-shadow:0 1px 5px rgba(0,0,0,.2);background:#c7a590}
.nav-arrow{position:absolute;top:2383px;width:31px;height:31px;border-radius:50%;display:flex;align-items:center;justify-content:center}

/* footer */
.site-footer{position:absolute;left:0;top:2672px;width:1200px;height:383px;background:var(--navy);color:#b8c0cc}
.site-footer .brand{top:66px;color:#fff}
.foot-about{position:absolute;left:134px;top:140px;width:200px;font-size:14px;line-height:22px}
.social{position:absolute;top:222px;width:36px;height:36px;border-radius:50%;background:#1f2c44}
.foot-col{position:absolute;top:68px}
.foot-col h4{font-family:var(--serif);font-weight:600;font-size:20px;color:#fff;margin-bottom:14px}
.foot-col li{list-style:none;font-size:15px;line-height:28.5px}
.email{position:absolute;left:813px;top:144px;width:251px;height:45px;background:#1e2b42;border-radius:4px;font-size:15px;padding:13px 17px}
.subscribe{position:absolute;left:813px;top:202px;width:251px;height:45px;background:var(--blue);border-radius:4px;color:#fff;font-size:16px;display:flex;align-items:center;justify-content:center}
.foot-rule{position:absolute;left:134px;top:333px;width:930px;height:1px;background:#22304a}
.copyright{position:absolute;left:0;top:349px;width:1200px;text-align:center;font-size:13px}
</style>
</head>
<body>

<header class="site-header">
  <div class="brand">Talented<small>Veroka</small></div>
  <div class="contact-box">
    <svg width="28" height="28" viewBox="0 0 24 24" fill="none" stroke="#0b56a4" stroke-width="1.5"><path d="M5 3h4l2 5-2.5 1.5a11 11 0 0 0 6 6L16 13l5 2v4a2 2 0 0 1-2 2A17 17 0 0 1 3 5a2 2 0 0 1 2-2z"/></svg>
    <div><div class="label">HAVE ANY QUESTION</div><div class="phone">123-555-0148</div></div>
  </div>
  <a class="btn-pill btn-outline">LOOKING FOR A JOB</a>
  <a class="btn-pill btn-solid">LOOKING FOR A EMPLOYERS</a>
  <div class="header-rule"></div>
  <nav>
    <a class="main-nav" style="left:134px">HOME</a>
    <a class="main-nav" style="left:222px">JOBS</a>
    <a class="main-nav" style="left:300px">FOR EMPLOYEES</a>
    <a class="main-nav" style="left:449px">FOR EMPLOYERS</a>
    <a class="main-nav" style="left:599px">CONTACT US</a>
    <a class="main-nav" style="left:954px;top:101px">LOGIN / REGISTER</a>
  </nav>
</header>

<section class="hero">
  <div class="hero-photo" role="img" aria-label="Five smiling professionals standing with arms crossed against a grey wall"></div>
  <h1 class="hero-title">FIND YOUR <span class="tag">DESIRE</span> JOB</h1>
  <p class="hero-sub">Find Jobs, Employment &amp; Career Opportunities</p>
</section>

<form class="search-bar">
  <div class="cat">
    <svg width="18" height="18" viewBox="0 0 18 18" fill="none" stroke="#9aa0a8" stroke-width="1.3"><rect x="1" y="1" width="6.5" height="6.5" rx="1"/><rect x="10.5" y="1" width="6.5" height="6.5" rx="1"/><rect x="1" y="10.5" width="6.5" height="6.5" rx="1"/><rect x="10.5" y="10.5" width="6.5" height="6.5" rx="1"/></svg>
    Choose Categories
  </div>
  <div class="sep"></div>
  <div class="kw">
    <svg width="18" height="18" viewBox="0 0 18 18" fill="none" stroke="#9aa0a8" stroke-width="1.5"><circle cx="7.5" cy="7.5" r="6"/><path d="M12 12l5 5"/></svg>
    Job title, Keywords, or Company
  </div>
  <div class="go">Search Job</div>
</form>

<section>
  <svg class="abs" style="left:0;top:890px" width="300" height="406" viewBox="0 0 300 406"><polygon points="0,95 134,0 134,330 90,406 0,406" fill="#f1f2f3"/><polygon points="134,330 280,230 300,230 90,406" fill="#f1f2f3"/></svg>
  <article class="split-card" style="left:134px">
    <h2>Looking for a Job?</h2>
    <p>Our ability to match the right employee with the right employer has helped many candidates in making life changing move to Australia and to become PERMANENT RESIDENT of Australia.</p>
  </article>
  <article class="split-card" style="left:617px">
    <h2>Looking for Employees?</h2>
    <p>We know, how difficult it is to get the skilled labour force to help with business growth and expansion . That is why we search, screen and select only the best suitable candidates with all documents ready to apply for visa which will dramatically save your time and money.</p>
  </article>
  <div class="abs" role="img" aria-label="Blue business person icon" style="left:573px;top:943px;width:52px;height:138px;background:var(--blue);border-radius:26px 26px 6px 6px"></div>
  <a class="pill-link" style="left:267px;width:182px">Looking for a job</a>
  <a class="pill-link" style="left:726px;width:230px;top:1119px">Looking for Employees</a>
  <p class="call-line">Call us today and let us help you expand your business.</p>
</section>

<section class="featured">
  <svg class="abs" style="right:0;top:300px" width="300" height="360" viewBox="0 0 300 360"><path d="M300 30 C230 0 180 40 190 110 L170 310 L250 360 L300 360 Z" fill="#1c66b2"/></svg>
  <h2 class="section-title" style="top:68px;color:#fff">FEATURED<span class="tag" style="background:#fff;color:var(--blue)">JOB</span>POSTS</h2>

  <article class="job-card" style="left:135px;top:165px">
    <div class="co">ORRA</div><span class="badge">FULL TIME</span>
    <h3>Lorem Ipsum Dolor Sit Amet</h3>
    <div class="meta"><svg width="14" height="14" viewBox="0 0 14 14" fill="none" stroke="#666" stroke-width="1.2"><path d="M13 1L1 6l5 2 2 5z"/></svg>Brisbane, Queensland.<em>5 Months Ago</em></div>
    <p>Lorem ipsum dolor sit amet, consectetur adipiscing elit, sed do eiusmod tempor incididunt ut labore...</p>
    <a class="apply">APPLY NOW</a>
  </article>
  <article class="job-card" style="left:610px;top:165px">
    <div class="co">ORRA</div><span class="badge">FULL TIME</span>
    <h3>Lorem Ipsum Dolor Sit Amet</h3>
    <div class="meta"><svg width="14" height="14" viewBox="0 0 14 14" fill="none" stroke="#666" stroke-width="1.2"><path d="M13 1L1 6l5 2 2 5z"/></svg>Brisbane, Queensland.<em>5 Months Ago</em></div>
    <p>Lorem ipsum dolor sit amet, consectetur adipiscing elit, sed do eiusmod tempor incididunt ut labore...</p>
    <a class="apply">APPLY NOW</a>
  </article>
  <article class="job-card" style="left:135px;top:384px">
    <div class="co">ORRA</div><span class="badge">FULL TIME</span>
    <h3>Lorem Ipsum Dolor Sit Amet</h3>
    <div class="meta"><svg width="14" height="14" viewBox="0 0 14 14" fill="none" stroke="#666" stroke-width="1.2"><path d="M13 1L1 6l5 2 2 5z"/></svg>Brisbane, Queensland.<em>5 Months Ago</em></div>
    <p>Lorem ipsum dolor sit amet, consectetur adipiscing elit, sed do eiusmod tempor incididunt ut labore...</p>
    <a class="apply">APPLY NOW</a>
  </article>
  <article class="job-card" style="left:610px;top:384px">
    <div class="co">ORRA</div><span class="badge">FULL TIME</span>
    <h3>Lorem Ipsum Dolor Sit Amet</h3>
    <div class="meta"><svg width="14" height="14" viewBox="0 0 14 14" fill="none" stroke="#666" stroke-width="1.2"><path d="M13 1L1 6l5 2 2 5z"/></svg>Brisbane, Queensland.<em>5 Months Ago</em></div>
    <p>Lorem ipsum dolor sit amet, consectetur adipiscing elit, sed do eiusmod tempor incididunt ut labore...</p>
    <a class="apply">APPLY NOW</a>
  </article>
</section>

<section>
  <h2 class="section-title" style="top:2025px;color:var(--blue)">OUR<span class="tag" style="background:var(--blue);color:#fff">USERS</span>LOVE US.</h2>
  <div class="tabs"><span class="on">Employers</span><span>Candidates</span></div>

  <div class="quote-card">
    <svg class="abs" style="left:390px;top:62px" width="95" height="80" viewBox="0 0 95 80"><polygon points="0,0 38,0 38,40 0,80" fill="#e3ecf6"/><polygon points="54,0 95,0 95,40 54,80" fill="#e3ecf6"/></svg>
    <div class="abs" style="left:182px;top:72px;color:#f07a0a;font-size:18px;letter-spacing:2px">★★★★★</div>
    <div class="abs" style="left:182px;top:98px;font-family:var(--serif);font-weight:500;font-size:26px;color:var(--ink)">JOHN DOE</div>
    <div class="abs" style="left:181px;top:135px;font-size:17px;color:var(--text)">Ceo &nbsp;at Brisbane, Queensland.</div>
    <div class="abs" style="left:182px;top:175px;width:290px;height:1px;background:#d8dce0"></div>
    <p class="abs" style="left:182px;top:192px;width:290px;font-size:15px;line-height:26px">Lorem ipsum dolor sit amet, consectetur adipisicing elit, sed do eiusmod tempor incididunt ut labore...</p>
    <div class="abs" style="left:182px;top:287px;display:flex;gap:10px;align-items:center;color:var(--blue);font-size:15px">
      <svg width="30" height="30" viewBox="0 0 30 30"><circle cx="15" cy="15" r="15" fill="#0b56a4"/><polygon points="12,9 21,15 12,21" fill="#fff"/></svg>Watch the video
    </div>
  </div>
  <div class="person-photo" role="img" aria-label="Portrait of a smiling man in a white t-shirt with arms crossed"></div>
  <div class="avatar" role="img" aria-label="Reviewer portrait" style="left:206px;top:2329px;width:42px;height:42px"></div>
  <div class="avatar" role="img" aria-label="Reviewer portrait" style="left:208px;top:2387px;background:#d9cfc8"></div>
  <div class="avatar" role="img" aria-label="Reviewer portrait" style="left:208px;top:2434px;background:#d8bfae"></div>
  <div class="nav-arrow" style="left:104px;background:#7fa6d2"><svg width="16" height="12" viewBox="0 0 16 12" fill="none" stroke="#fff" stroke-width="1.5"><path d="M15 6H1M6 1L1 6l5 5"/></svg></div>
  <div class="nav-arrow" style="left:1064px;background:var(--blue)"><svg width="16" height="12" viewBox="0 0 16 12" fill="none" stroke="#fff" stroke-width="1.5"><path d="M1 6h14M10 1l5 5-5 5"/></svg></div>
</section>

<footer class="site-footer">
  <div class="brand">Talented<small>Veroka</small></div>
  <p class="foot-about">Lorem ipsum dolor sit amet, consectetur adipiscing elit, sed do eiusmod tempor</p>
  <a class="social" style="left:134px" aria-label="Social profile one"></a>
  <a class="social" style="left:182px;background:var(--blue)" aria-label="Social profile two"></a>
  <a class="social" style="left:229px" aria-label="Social profile three"></a>
  <div class="foot-col" style="left:411px"><h4>Quick Links</h4><ul><li>Home</li><li>Jobs</li><li>For Employees</li><li>For Employers</li><li>Contact Us</li></ul></div>
  <div class="foot-col" style="left:615px"><h4>Other links</h4><ul><li>Login</li><li>Register</li></ul></div>
  <div class="foot-col" style="left:812px"><h4>Join US</h4><ul><li>Subscribe To Our Newsletters</li></ul></div>
  <div class="email">Email address</div>
  <a class="subscribe">Subscribe Now</a>
  <div class="foot-rule"></div>
  <p class="copyright">Copyright © 2022 Talented Veroka All rights reserved.</p>
</footer>

</body>
</html>
```